Design our letter, business card, powerpoint and more

We have a logo and want a design for our business use. Letters (word template), business card (for printing) powerpoint presentation (template) and more.

```html
<!DOCTYPE html>
<html lang="en">
<head>
<meta charset="UTF-8">
<title>Our Company Services</title>
<link href="https://fonts.googleapis.com/css2?family=Lato:wght@700&family=Open+Sans:wght@400&family=Arimo:wght@400&display=swap" rel="stylesheet">
<style>
  :root {
    --brand-blue: #346aa0;
    --hero-top: #4a7db3;
    --hero-bottom: #3f72a8;
    --white: #ffffff;
    --ink: #111111;
  }
  * { box-sizing: border-box; margin: 0; padding: 0; }
  html, body { width: 1200px; height: 675px; overflow: hidden; background: var(--white); }
  .slide { position: relative; width: 1200px; height: 675px; background: var(--white); overflow: hidden; }

  .hero {
    position: absolute; left: 0; top: 0; width: 1200px; height: 338px;
    background: linear-gradient(100deg, #3d6ea6 0%, #5384ba 45%, #5f8fc0 70%, #5b8db2 100%);
  }
  .hero-title {
    position: absolute; left: 0; top: 62px; width: 1200px; text-align: center;
    font-family: 'Lato', sans-serif; font-weight: 700; font-size: 48px; line-height: 1.2;
    color: var(--white);
  }
  .hero-intro {
    position: absolute; left: 232px; top: 141px; width: 736px;
    font-family: 'Open Sans', sans-serif; font-size: 18px; line-height: 24px;
    color: var(--white); text-align: justify; text-align-last: center;
  }

  .service { position: absolute; top: 277px; width: 300px; text-align: center; }
  .service-badge {
    width: 120px; height: 120px; margin: 0 auto; border-radius: 50%;
    background: var(--white); box-shadow: 2px 4px 5px rgba(0,0,0,0.45);
    display: flex; align-items: center; justify-content: center;
  }
  .service-ring {
    width: 106px; height: 106px; border-radius: 50%; border: 4px solid var(--brand-blue);
    display: flex; align-items: center; justify-content: center;
  }
  .service-icon { width: 58px; height: 58px; }
  .service-title {
    margin-top: 48px; font-family: 'Lato', sans-serif; font-weight: 700;
    font-size: 24px; line-height: 30px; color: var(--ink);
  }
  .service-text {
    margin: 8px auto 0; width: 240px; font-family: 'Arimo', Arial, sans-serif;
    font-size: 21.5px; line-height: 27.5px; color: var(--ink);
  }
</style>
</head>
<body>
<div class="slide">
  <div class="hero" role="img" aria-label="Blue-tinted photograph of a modern office building beside a tree-lined street"></div>
  <h1 class="hero-title">Our Company Services</h1>
  <p class="hero-intro">Pellentesque habitant morbi tristique senectus et netus et malesuada fames ac turpis egestas. Nunc ut elementum ligula. Quisque consequat justo ligula, vitae laoreet magna bibendum at.</p>

  <div class="service" style="left:98px;">
    <div class="service-badge"><div class="service-ring">
      <svg class="service-icon" viewBox="0 0 100 100"><path fill="#346aa0" d="M8 52 L50 14 L92 52 L86 58 L50 26 L14 58 Z M70 18 H80 V38 L70 29 Z M22 58 L50 33 L78 58 V90 H22 Z"/><rect x="32" y="62" width="12" height="12" fill="#fff"/><rect x="56" y="62" width="12" height="12" fill="#fff"/></svg>
    </div></div>
    <h2 class="service-title">List of services</h2>
    <p class="service-text">Vivamus bibendum leo sit amet lectus ullamcorper tristique.</p>
  </div>

  <div class="service" style="left:454px;">
    <div class="service-badge"><div class="service-ring">
      <svg class="service-icon" viewBox="0 0 100 100"><path fill="#346aa0" d="M8 52 L50 14 L92 52 L86 58 L50 26 L14 58 Z M70 18 H80 V38 L70 29 Z M22 58 L50 33 L78 58 V90 H22 Z"/><rect x="32" y="62" width="12" height="12" fill="#fff"/><rect x="56" y="62" width="12" height="12" fill="#fff"/></svg>
    </div></div>
    <h2 class="service-title">List of services</h2>
    <p class="service-text">Vivamus bibendum leo sit amet lectus ullamcorper tristique.</p>
  </div>

  <div class="service" style="left:802px;">
    <div class="service-badge"><div class="service-ring">
      <svg class="service-icon" viewBox="0 0 100 100"><path fill="#346aa0" d="M8 52 L50 14 L92 52 L86 58 L50 26 L14 58 Z M70 18 H80 V38 L70 29 Z M22 58 L50 33 L78 58 V90 H22 Z"/><rect x="32" y="62" width="12" height="12" fill="#fff"/><rect x="56" y="62" width="12" height="12" fill="#fff"/></svg>
    </div></div>
    <h2 class="service-title">List of services</h2>
    <p class="service-text">Vivamus bibendum leo sit amet lectus ullamcorper tristique.</p>
  </div>
</div>
</body>
</html>
```